Announcing New Mental Health Practice

We need a front & back color postcard design that will be mailed to prospective clients (4"x6") and other businesses in the area to grow our client base. We originally targeted children and adolescent clients only but we now want to include adults and couples - including seniors!
We have several clinicians on staff who specialize in Play Therapy, Dialectical behavior therapy (DBT), Cognitive behavioral therapy (CBT) and we also have two certified therapy dogs!
We are accepting new clients and we currently do not have a wait list! We accept most commercial insurance companies and are part of the Brookfield Health Alliance.
What is Brookfield Health Alliance?
Brookfield Health Alliance is a partnership between medical professionals and Veridane Medical Brookfield and is the largest Physician Hospital Organization (PHO) in southwestern Michigan who share a commitment to excellence.
We are located inside The Whole Wellness Renewal Hub at 4173 Partridge Lane, Saint Joseph, MI 49372. (also include map). Call us at 269-815-4027 to make an appointment.
Postcard - to be mailed.
Attaching some stock photos but please feel free to add or use other photos that promote counseling / mental health services - but we will not purchase additional photos! I also added a design that looked nice to us - but I do not want to copy it - we want something original for us.
Our website isn't great, but the address is:
www.findyourcalmpath.example

Target Market(s)

Adult Clients

Industry/Entity Type

Mental Health

Colors
0054AA
0677BA
7BADD7
CADEEF
E8F1F8
00AB8E
00BBA5
67D7C9
C6EFE9
E9F9F6
6B429C
8869AF
B7A5CE
E3DAEB
F3F0F8

Requirements
Should not have
• Typos; broken English

```html
<!DOCTYPE html>
<html lang="en">
<head>
<meta charset="utf-8">
<title>Calm Path Counseling – Postcard</title>
<link href="https://fonts.googleapis.com/css2?family=Montserrat:wght@400;500;700;800&family=Antonio:wght@300;700&display=swap" rel="stylesheet">
<style>
  :root{
    --backdrop:#b3b3b3;
    --paper:#ffffff;
    --green:#00a04b;
    --green-light:#8dc63f;
    --green-pale:#c8e39c;
    --orange:#f7a823;
    --blue:#0677ba;
    --ink:#222222;
    --rule:#9a9a9a;
    --stamp:#a7a9ac;
  }
  *{margin:0;padding:0;box-sizing:border-box}
  html,body{width:1200px;height:1117px;overflow:hidden}
  body{background:var(--backdrop);font-family:"Montserrat",sans-serif;color:var(--ink);position:relative}
  .postcard{position:absolute;left:227px;width:747px;height:497px;background:var(--paper);overflow:hidden}
  .postcard--front{top:50px}
  .postcard--back{top:569px}
  .postcard__shapes{position:absolute;inset:0;width:100%;height:100%}
  .abs{position:absolute}

  .brand{text-align:center;color:var(--ink)}
  .brand__name{font-weight:700;color:var(--green);letter-spacing:.5px}
  .brand__tagline{font-weight:400;line-height:1.15}
  .front-brand{left:40px;top:80px;width:220px}
  .front-brand .brand__name{font-size:24px;line-height:1.1;margin-bottom:14px}
  .front-brand .brand__tagline{font-size:12.5px}

  .services{left:50px;top:280px;width:310px;color:#fff;font-weight:700;font-size:15.4px;line-height:1.2}
  .headline{left:50px;top:400px;color:#fff;font-weight:800;font-size:33px;line-height:1}
  .insurance{left:469px;top:305px;width:120px;font-size:10.8px;line-height:1.2}
  .network-name{color:var(--blue);font-weight:700;text-align:center;line-height:1.15;display:flex;align-items:center;justify-content:center}
  .front-network{left:592px;top:306px;width:130px;height:76px;font-size:15px}

  .call-box{text-align:center;border-radius:12px;white-space:nowrap}
  .call-box__line{font-family:"Antonio",sans-serif;font-weight:300;line-height:1}
  .call-box__line strong{font-weight:700}
  .call-box__sub{font-weight:700;line-height:1.1}
  .front-call{left:452px;top:406px;width:270px;height:68px;border:2.5px solid var(--orange);padding-top:9px}
  .front-call .call-box__line{font-size:29px;color:var(--ink)}
  .front-call .call-box__sub{font-size:14.5px;margin-top:4px}

  .about-title{left:49px;top:37px;width:280px;color:var(--green);font-weight:800;font-size:26px;line-height:1.05}
  .about-body{left:49px;top:102px;width:236px;font-size:11.4px;line-height:1.28}
  .map{left:46px;top:271px;width:153px;height:102px;border:3px solid #fff;border-radius:10px;background:linear-gradient(135deg,#e6efe3,#cfe3d4 55%,#a9cbe8)}
  .location{left:216px;top:275px;width:150px;color:#fff;font-size:13.5px;line-height:1.2}
  .back-call{left:46px;top:389px;width:350px;height:83px;border:3px solid #fff;padding-top:12px}
  .back-call .call-box__line{font-size:35px;color:#fff}
  .back-call .call-box__sub{font-size:17px;color:#fff;margin-top:3px}

  .back-brand{left:385px;top:30px;width:100px}
  .back-brand .brand__name{font-size:12px;line-height:1.1;margin-bottom:8px}
  .back-brand .brand__tagline{font-size:6.5px}
  .back-network{left:496px;top:40px;width:107px;height:61px;font-size:11.5px}
  .stamp{left:634px;top:30px;width:77px;height:76px;background:var(--stamp)}
  .address-line{left:482px;width:229px;height:0;border-top:1.5px solid var(--rule)}
</style>
</head>
<body>

<section class="postcard postcard--front" aria-label="Postcard front">
  <svg class="postcard__shapes" viewBox="0 0 996 663" preserveAspectRatio="none">
    <defs>
      <linearGradient id="photoTone" x1="0" y1="0" x2="1" y2="1">
        <stop offset="0" stop-color="#7fae4a"/>
        <stop offset=".5" stop-color="#d9c29c"/>
        <stop offset="1" stop-color="#5f9a3c"/>
      </linearGradient>
    </defs>
    <path d="M420 0 H996 V258 C880 345 700 375 560 355 C480 320 432 200 420 0 Z" fill="var(--orange)"/>
    <path role="img" aria-label="Photo of a certified therapy dog wearing a red harness on grass" d="M420 0 H996 V240 C880 325 700 352 560 336 C482 300 436 190 420 0 Z" fill="url(#photoTone)"/>
    <path d="M0 345 C160 300 330 290 480 320 L500 380 L0 380 Z" fill="var(--orange)"/>
    <path d="M0 362 C160 320 330 312 470 336 C530 420 545 540 505 663 H0 Z" fill="var(--green)"/>
    <path d="M350 0 H420 C432 180 500 300 545 380 C585 470 570 580 535 663 H485 C530 560 540 470 500 390 C440 280 370 160 350 0 Z" fill="var(--green-light)"/>
    <path d="M420 0 H438 C448 170 515 290 560 375 C598 465 585 575 552 663 H535 C570 580 585 470 545 380 C500 300 432 180 420 0 Z" fill="var(--green-pale)"/>
    <path d="M545 663 C600 645 700 637 996 637 V641 C700 641 610 650 560 663 Z" fill="var(--orange)"/>
  </svg>

  <div class="brand front-brand abs">
    <p class="brand__name">Calm Path Counseling</p>
    <p class="brand__tagline">Counseling &amp; Support for Children, Families and Adults</p>
  </div>

  <p class="services abs">We have several clinicians on staff who specialize in Play Therapy, Dialectical behavior therapy (DBT), Cognitive behavioral therapy (CBT) and we also have two certified therapy dogs!</p>
  <h1 class="headline abs">We are accepting<br>new patients</h1>

  <p class="insurance abs">We accept most commercial insurance companies and are part of the Brookfield Health Alliance.</p>
  <p class="network-name front-network abs">Brookfield Health Alliance</p>

  <div class="call-box front-call abs">
    <p class="call-box__line">CALL US AT <strong>269-815-4027</strong></p>
    <p class="call-box__sub">to make an appointment.</p>
  </div>
</section>

<section class="postcard postcard--back" aria-label="Postcard back">
  <svg class="postcard__shapes" viewBox="0 0 996 663" preserveAspectRatio="none">
    <path d="M0 320 C160 280 330 275 470 300 L480 345 L0 345 Z" fill="var(--orange)"/>
    <path d="M0 338 C160 300 330 292 460 318 C510 380 540 560 490 663 H0 Z" fill="var(--green)"/>
    <path d="M420 0 H470 C480 130 560 240 590 360 C625 490 560 600 520 663 H470 C525 590 575 480 545 370 C515 250 440 140 420 0 Z" fill="var(--green-light)"/>
    <path d="M470 0 H485 C495 130 580 240 610 360 C645 490 580 600 540 663 H520 C560 600 625 490 590 360 C560 240 480 130 470 0 Z" fill="var(--green-pale)"/>
  </svg>

  <h2 class="about-title abs">What is Brookfield Health Alliance?</h2>
  <p class="about-body abs">Brookfield Health Alliance is a partnership between medical professionals and Veridane Medical Brookfield and is the largest Physician Hospital Organization (PHO) in southwestern Michigan who share a commitment to excellence.</p>

  <div class="map abs" role="img" aria-label="Map showing the office location in Saint Joseph, Michigan"></div>
  <p class="location abs">We are located inside The Whole Wellness Renewal Hub at 4173 Partridge Lane, Saint Joseph, MI 49372</p>

  <div class="call-box back-call abs">
    <p class="call-box__line">CALL US AT <strong>269-815-4027</strong></p>
    <p class="call-box__sub">to make an appointment.</p>
  </div>

  <div class="brand back-brand abs">
    <p class="brand__name">Calm Path Counseling</p>
    <p class="brand__tagline">Counseling &amp; Support for Children, Families and Adults</p>
  </div>
  <p class="network-name back-network abs">Brookfield Health Alliance</p>
  <div class="stamp abs" aria-label="Stamp area"></div>

  <div class="address-line abs" style="top:213px"></div>
  <div class="address-line abs" style="top:252px"></div>
  <div class="address-line abs" style="top:292px"></div>
  <div class="address-line abs" style="top:331px"></div>
  <div class="address-line abs" style="top:370px"></div>
</section>

</body>
</html>
```